Host Home Needed Flier

We need a refresh of this flier to be more modern and informative. We'll use the new flier as a template for all our centers across the United States-therefore, it should be editable. We don't typically use stock photos (in order to look authentic to our clients) be would be open to a stock photo if it was relevant. We have a lot of work coming up and would like to establish a relationship with a designer. We are an international company who have been business for over 30 years working with international students ages 8-30. Our marketing/branding colors should be fresh and appeal to young people from all over the globe. We love the color blue in every shade and we love innovative cool fonts.

```html
<!DOCTYPE html>
<html lang="en">
<head>
<meta charset="utf-8">
<title>Host Family Flier – Two Options</title>
<link rel="stylesheet" href="https://fonts.googleapis.com/css2?family=Montserrat:wght@500;600;700;800&family=Roboto+Condensed:wght@300;400&display=swap">
<style>
  :root {
    --board: #98a4ae;
    --paper: #ffffff;
    --navy: #1a4b80;
    --blue: #1b5d9d;
    --panel-grey: #e4e4e4;
    --orange: #e8893b;
    --orange-light: #f0a66a;
    --teal: #1aab9b;
    --teal-light: #6fcdc2;
    --ink-dark: #1b1b1b;
  }
  * { box-sizing: border-box; margin: 0; padding: 0; }
  html, body { width: 1200px; height: 885px; overflow: hidden; }
  body { background: var(--board); position: relative; font-family: 'Montserrat', sans-serif; }

  .flier {
    position: absolute; top: 34px; width: 558px; height: 789px;
    background: var(--paper);
    box-shadow: 0 2px 8px rgba(0,0,0,.25);
  }
  .flier--photo-free { left: 28px; --accent: var(--orange); --accent-light: var(--orange-light); }
  .flier--stock { left: 615px; --accent: var(--teal); --accent-light: var(--teal-light); }

  .brand { position: absolute; left: 28px; top: 20px; display: flex; align-items: center; gap: 14px; }
  .brand-mark { width: 54px; height: 54px; background: var(--navy); }
  .brand-name { font-weight: 700; font-size: 19.5px; color: var(--navy); letter-spacing: .6px; line-height: 1; }
  .brand-tagline { font-weight: 500; font-size: 12.6px; color: var(--navy); letter-spacing: .3px; margin-top: 6px; }

  .photo { position: absolute; }
  .photo--hero { left: 34px; top: 94px; width: 493px; height: 262px; }
  .photo--class { left: 252px; top: 366px; width: 132px; height: 103px; }
  .photo--campus { left: 394px; top: 366px; width: 132px; height: 103px; }
  .photo--trip { left: 252px; top: 479px; width: 132px; height: 105px; }
  .photo--friends { left: 394px; top: 479px; width: 132px; height: 105px; }
  .photo--group { left: 34px; top: 518px; width: 209px; height: 66px; }

  .tone-sky { background: linear-gradient(180deg, #3d78c4 0%, #6d93bf 45%, #4a3f3a 100%); }
  .tone-crowd { background: linear-gradient(135deg, #c7b7a6 0%, #5a7fb8 40%, #b8d45a 75%, #d9b59a 100%); }
  .tone-class { background: linear-gradient(180deg, #e8e6e0 0%, #c9c5be 60%, #2e3845 100%); }
  .tone-campus { background: linear-gradient(180deg, #6f8a5b 0%, #35507e 55%, #2a2a2a 100%); }
  .tone-trip { background: linear-gradient(180deg, #9b8aa4 0%, #c2503e 55%, #4d7fb3 100%); }
  .tone-friends { background: linear-gradient(180deg, #4d6b45 0%, #e9e4dc 55%, #3d5d8a 100%); }
  .tone-group { background: linear-gradient(180deg, #b7c2c7 0%, #7d8a78 45%, #2c2c34 100%); }

  .headline-box {
    position: absolute; left: 18px; top: 244px; width: 233px; height: 271px;
    background: var(--paper); padding: 4px;
  }
  .headline {
    width: 100%; height: 100%; background: var(--blue); color: #fff;
    padding: 30px 0 0 11px; font-weight: 800; text-transform: uppercase;
  }
  .headline-line { font-size: 24px; line-height: 31px; }
  .headline-punch { font-size: 47px; line-height: 52px; margin-top: 4px; }

  .offer { position: absolute; left: 34px; top: 596px; width: 493px; height: 132px; }
  .offer svg { position: absolute; inset: 0; }
  .offer-news {
    position: absolute; left: 0; top: 0; width: 260px; height: 132px;
    display: flex; align-items: center; justify-content: center; text-align: center;
    font-family: 'Roboto Condensed', sans-serif; font-weight: 400; font-size: 23px;
    line-height: 28.5px; color: var(--navy); text-transform: uppercase;
  }
  .offer-pay {
    position: absolute; left: 283px; top: 0; width: 200px; height: 132px;
    display: flex; flex-direction: column; justify-content: center; align-items: center;
    color: #fff; font-weight: 700; white-space: nowrap;
  }
  .offer-pay-label { font-size: 24px; line-height: 34px; }
  .offer-pay-amount { font-size: 25px; line-height: 38px; font-weight: 800; }

  .contact {
    position: absolute; left: 0; right: 0; top: 745px;
    display: flex; justify-content: center; align-items: center; gap: 10px;
    color: var(--navy); font-weight: 500; font-size: 18.5px; letter-spacing: .3px;
  }
  .contact-item { display: flex; align-items: center; gap: 6px; }
  .contact svg { width: 18px; height: 18px; }
  .flier--stock .contact svg { color: var(--teal); }

  .caption {
    position: absolute; top: 839px; width: 558px; text-align: center;
    font-family: 'Roboto Condensed', sans-serif; font-weight: 400; font-size: 23px;
    color: var(--ink-dark); text-transform: uppercase;
  }
  .caption--photo-free { left: 28px; }
  .caption--stock { left: 615px; }
</style>
</head>
<body>

  <section class="flier flier--photo-free">
    <header class="brand">
      <div class="brand-mark"></div>
      <div>
        <div class="brand-name">GLOBAL STUDENT HOMESTAYS</div>
        <div class="brand-tagline">Remarkable American Experiences for International Students</div>
      </div>
    </header>

    <div class="photo photo--hero tone-sky" role="img" aria-label="Host mother with three smiling students outdoors under a blue sky"></div>
    <div class="photo photo--class tone-class" role="img" aria-label="Teachers standing in front of a classroom whiteboard"></div>
    <div class="photo photo--campus tone-campus" role="img" aria-label="Host mother with two students on campus"></div>
    <div class="photo photo--trip tone-trip" role="img" aria-label="Students posing together on an outing"></div>
    <div class="photo photo--friends tone-friends" role="img" aria-label="Two students smiling outdoors"></div>
    <div class="photo photo--group tone-group" role="img" aria-label="Group of students standing in a row outdoors"></div>

    <div class="headline-box">
      <div class="headline">
        <div class="headline-line">Become</div>
        <div class="headline-line">a host</div>
        <div class="headline-line">for an</div>
        <div class="headline-line">international</div>
        <div class="headline-line">student</div>
        <div class="headline-punch">Today!</div>
      </div>
    </div>

    <div class="offer">
      <svg viewBox="0 0 493 132" width="493" height="132">
        <rect x="0" y="0" width="493" height="132" fill="var(--panel-grey)"/>
        <polygon points="241,0 256,0 278,66 256,132 241,132 263,66" fill="var(--accent-light)"/>
        <polygon points="256,0 493,0 493,132 256,132 278,66" fill="var(--accent)"/>
        <path d="M266 7 H487 V125 H266 L283 66 Z" fill="none" stroke="#fff" stroke-width="1.3" stroke-dasharray="5 3"/>
      </svg>
      <div class="offer-news">International<br>students attending<br>Bayview arriving now!</div>
      <div class="offer-pay">
        <div class="offer-pay-label">HOSTS PAID</div>
        <div class="offer-pay-amount">$1000/month</div>
      </div>
    </div>

    <footer class="contact">
      <span class="contact-item">
        <svg viewBox="0 0 20 20"><circle cx="10" cy="10" r="8.5" fill="none" stroke="currentColor" stroke-width="1.5"/><ellipse cx="10" cy="10" rx="3.8" ry="8.5" fill="none" stroke="currentColor" stroke-width="1.3"/><path d="M1.5 10H18.5M3 5.5H17M3 14.5H17" stroke="currentColor" stroke-width="1.3"/></svg>
        globalhomestays.example
      </span>
      <span class="contact-item">
        <svg viewBox="0 0 20 20"><path d="M5 2.5l3 3.5-1.8 2a10 10 0 0 0 5.8 5.8l2-1.8 3.5 3-2 2.5C9 17 3 11 2.5 4.5z" fill="none" stroke="currentColor" stroke-width="1.5" stroke-linejoin="round"/></svg>
        555-014-2290
      </span>
    </footer>
  </section>

  <section class="flier flier--stock">
    <header class="brand">
      <div class="brand-mark"></div>
      <div>
        <div class="brand-name">GLOBAL STUDENT HOMESTAYS</div>
        <div class="brand-tagline">Remarkable American Experiences for International Students</div>
      </div>
    </header>

    <div class="photo photo--hero tone-crowd" role="img" aria-label="Crowd of cheering young people from many backgrounds raising their arms"></div>
    <div class="photo photo--class tone-class" role="img" aria-label="Teachers standing in front of a classroom whiteboard"></div>
    <div class="photo photo--campus tone-campus" role="img" aria-label="Host mother with two students on campus"></div>
    <div class="photo photo--trip tone-trip" role="img" aria-label="Students posing together on an outing"></div>
    <div class="photo photo--friends tone-friends" role="img" aria-label="Two students smiling outdoors"></div>
    <div class="photo photo--group tone-group" role="img" aria-label="Group of students standing in a row outdoors"></div>

    <div class="headline-box">
      <div class="headline">
        <div class="headline-line">Become</div>
        <div class="headline-line">a host</div>
        <div class="headline-line">for an</div>
        <div class="headline-line">international</div>
        <div class="headline-line">student</div>
        <div class="headline-punch">Today!</div>
      </div>
    </div>

    <div class="offer">
      <svg viewBox="0 0 493 132" width="493" height="132">
        <rect x="0" y="0" width="493" height="132" fill="var(--panel-grey)"/>
        <polygon points="241,0 256,0 278,66 256,132 241,132 263,66" fill="var(--accent-light)"/>
        <polygon points="256,0 493,0 493,132 256,132 278,66" fill="var(--accent)"/>
        <path d="M266 7 H487 V125 H266 L283 66 Z" fill="none" stroke="#fff" stroke-width="1.3" stroke-dasharray="5 3"/>
      </svg>
      <div class="offer-news">International<br>students attending<br>Bayview arriving now!</div>
      <div class="offer-pay">
        <div class="offer-pay-label">HOSTS PAID</div>
        <div class="offer-pay-amount">$1000/month</div>
      </div>
    </div>

    <footer class="contact">
      <span class="contact-item">
        <svg viewBox="0 0 20 20"><circle cx="10" cy="10" r="8.5" fill="none" stroke="currentColor" stroke-width="1.5"/><ellipse cx="10" cy="10" rx="3.8" ry="8.5" fill="none" stroke="currentColor" stroke-width="1.3"/><path d="M1.5 10H18.5M3 5.5H17M3 14.5H17" stroke="currentColor" stroke-width="1.3"/></svg>
        globalhomestays.example
      </span>
      <span class="contact-item">
        <svg viewBox="0 0 20 20"><path d="M5 2.5l3 3.5-1.8 2a10 10 0 0 0 5.8 5.8l2-1.8 3.5 3-2 2.5C9 17 3 11 2.5 4.5z" fill="none" stroke="currentColor" stroke-width="1.5" stroke-linejoin="round"/></svg>
        555-014-2290
      </span>
    </footer>
  </section>

  <div class="caption caption--photo-free">Without stock image</div>
  <div class="caption caption--stock">With stock image</div>

</body>
</html>
```